Design a compelling Tarnwell Business Card that will drive people to my site

I want a business card that I can give to people—less to tell them who I am and more to direct them to my website. My website is a portal for Crestlane Aquatics Officials and a place for people who want to become Crestlane Aquatics Officials.
I am uploading my official company logo as well as a business card mockup that I did on my own. Please feel free to completely stray from this design.
I've included a screen recording of the homepage of my website as well.
Target Market(s)
Crestlane Aquatics Officials and people who desire to become one
Contact Information for Business Card
website url
Look and feel
Each slider illustrates characteristics of the customer's brand and the style your logo design should communicate.

```html
<!DOCTYPE html>
<html lang="en">
<head>
<meta charset="UTF-8">
<title>Tarnwell Business Card</title>
<link href="https://fonts.googleapis.com/css2?family=Montserrat:wght@400;600;700&display=swap" rel="stylesheet">
<style>
  :root {
    --brand-blue: #3a55a5;
    --light-blue: #93a9d8;
    --ink: #2a2f3a;
    --card-white: #ffffff;
    --backdrop: #d6d6d6;
  }
  * { margin: 0; padding: 0; box-sizing: border-box; }
  html, body { width: 1200px; height: 802px; overflow: hidden; }
  body {
    background: var(--backdrop);
    font-family: 'Montserrat', sans-serif;
    position: relative;
  }
  .card {
    position: absolute;
    top: 246px;
    width: 540px;
    height: 309px;
    border-radius: 22px;
    overflow: hidden;
    box-shadow: 0 12px 28px rgba(0,0,0,0.22);
  }
  .card-front { left: 40px; background: var(--card-white); }
  .card-back { left: 620px; background: var(--brand-blue); }

  .front-wave { position: absolute; inset: 0; width: 540px; height: 309px; }

  .front-brand {
    position: absolute;
    left: 40px;
    top: 150px;
    font-size: 46px;
    font-weight: 700;
    color: var(--brand-blue);
    letter-spacing: -0.5px;
  }
  .front-divider {
    position: absolute;
    left: 258px;
    top: 60px;
    width: 1px;
    height: 150px;
    background: #c9d2ea;
  }
  .front-details { position: absolute; left: 278px; top: 62px; }
  .person-name { font-size: 22px; font-weight: 700; color: var(--brand-blue); line-height: 1.1; }
  .person-name .surname { color: var(--light-blue); }
  .person-title { font-size: 12.5px; color: var(--ink); margin-top: 3px; }
  .contact-list { list-style: none; margin-top: 16px; }
  .contact-item {
    display: flex; align-items: center; gap: 8px;
    font-size: 12.5px; color: var(--ink); margin-bottom: 7px;
  }
  .contact-icon { width: 13px; height: 13px; flex: none; }

  .back-texture { position: absolute; inset: 0;
    background:
      radial-gradient(circle at 82% 22%, rgba(255,255,255,0.12) 0 9%, transparent 10%),
      radial-gradient(circle at 12% 80%, rgba(255,255,255,0.10) 0 8%, transparent 9%),
      radial-gradient(circle at 60% 78%, rgba(255,255,255,0.10) 0 10%, transparent 11%),
      var(--brand-blue);
  }
  .back-brand {
    position: absolute; inset: 0;
    display: flex; align-items: center; justify-content: center;
    font-size: 68px; font-weight: 700; color: var(--card-white);
    letter-spacing: -1px;
  }
</style>
</head>
<body>
  <section class="card card-front">
    <svg class="front-wave" viewBox="0 0 540 309" aria-hidden="true">
      <path d="M0,262 C180,290 330,252 420,196 C470,166 510,150 540,145 L540,309 L0,309 Z" fill="#93a9d8"/>
      <path d="M0,274 C180,302 330,266 420,210 C470,180 510,164 540,159 L540,309 L0,309 Z" fill="#ffffff"/>
      <path d="M0,284 C180,310 330,278 420,222 C470,192 510,176 540,171 L540,309 L0,309 Z" fill="#3a55a5"/>
    </svg>
    <div class="front-brand">tarnwell</div>
    <div class="front-divider"></div>
    <div class="front-details">
      <p class="person-name">Marcus <span class="surname">Ellery</span></p>
      <p class="person-title">CEO &amp; Founder</p>
      <ul class="contact-list">
        <li class="contact-item">
          <svg class="contact-icon" viewBox="0 0 16 16"><path d="M3 1l3 3-1.5 2a9 9 0 0 0 5.5 5.5L12 10l3 3-2 2C7 15 1 9 1 3z" fill="#3a55a5"/></svg>
          (555) 014-2270
        </li>
        <li class="contact-item">
          <svg class="contact-icon" viewBox="0 0 16 16"><rect x="1" y="3" width="14" height="10" fill="#3a55a5"/><path d="M1 3l7 6 7-6" stroke="#fff" stroke-width="1.2" fill="none"/></svg>
          marcus@tarnwell.com
        </li>
        <li class="contact-item">
          <svg class="contact-icon" viewBox="0 0 16 16"><circle cx="8" cy="8" r="7" fill="#3a55a5"/><path d="M1 8h14M8 1c-3 4-3 10 0 14M8 1c3 4 3 10 0 14" stroke="#fff" stroke-width="0.9" fill="none"/></svg>
          www.tarnwell.com
        </li>
      </ul>
    </div>
  </section>

  <section class="card card-back">
    <div class="back-texture" role="img" aria-label="Soft bubble texture on blue water background"></div>
    <div class="back-brand">tarnwell</div>
  </section>
</body>
</html>
```